Construction Company

I'm a new construction company called Tembrik Construction. I want my card to look simple and clean. I have provided a sample of what I want the front to look like (Tembrik_Card.jpeg) and a back ground for the back of the (Tembrik_Card_Background.jpeg) - the background can be faded so my name and other information is more prominent.
Construction

```html
<!DOCTYPE html>
<html lang="en">
<head>
<meta charset="utf-8">
<title>Tembrik Construction – Business Card</title>
<link rel="stylesheet" href="https://fonts.googleapis.com/css2?family=Open+Sans:wght@400;600;700&display=swap">
<style>
  :root {
    --page: #1c1d1f;
    --card: #2b3a4d;
    --card-deep: #243245;
    --plan: #2f3f53;
    --orange: #f29a17;
    --light: #e6e9ee;
    --muted: #9aa5b3;
  }
  * { margin: 0; padding: 0; box-sizing: border-box; }
  html, body { width: 1200px; height: 900px; overflow: hidden; }
  body {
    background: var(--page);
    font-family: "Open Sans", Arial, sans-serif;
    position: relative;
  }
  .card {
    position: absolute;
    left: 280px;
    width: 640px;
    height: 366px;
    background: linear-gradient(160deg, var(--card) 0%, var(--card-deep) 100%);
    overflow: hidden;
  }
  .card--front { top: 52px; }
  .card--back { top: 482px; }

  .wordmark {
    color: var(--orange);
    font-weight: 600;
    letter-spacing: 0.01em;
    line-height: 1;
    white-space: nowrap;
  }
  .card--front .wordmark {
    position: absolute;
    left: 0; right: 0; top: 150px;
    text-align: center;
    font-size: 58px;
  }

  .floor-plan {
    position: absolute;
    left: 120px; top: 40px;
    width: 520px; height: 290px;
    background: radial-gradient(ellipse at 55% 50%, var(--plan) 0%, rgba(47,63,83,0.35) 70%, rgba(47,63,83,0) 100%);
  }

  .card--back .wordmark {
    position: absolute;
    left: 34px; top: 112px;
    font-size: 34px;
  }

  .holder {
    position: absolute;
    right: 34px; top: 34px;
    text-align: right;
  }
  .holder__name { color: var(--orange); font-weight: 700; font-size: 17px; }
  .holder__role { color: var(--light); font-weight: 700; font-size: 13px; margin-top: 2px; }
  .holder__license { color: var(--orange); font-size: 10px; margin-top: 8px; }

  .address {
    position: absolute;
    right: 34px; top: 196px;
    text-align: right;
    color: var(--muted);
    font-size: 15px;
    line-height: 1.35;
  }

  .contacts {
    position: absolute;
    left: 34px; bottom: 26px;
    list-style: none;
    color: var(--light);
    font-size: 16px;
    line-height: 1.45;
  }
  .contacts li { display: flex; align-items: center; gap: 10px; }
  .contacts svg { width: 14px; height: 14px; flex: none; }
</style>
</head>
<body>

<section class="card card--front" aria-label="Card front">
  <div class="wordmark">Tembrik Construction</div>
</section>

<section class="card card--back" aria-label="Card back">
  <div class="floor-plan" role="img" aria-label="Faded architectural floor plan background"></div>

  <div class="wordmark">Tembrik Construction</div>

  <div class="holder">
    <div class="holder__name">Daniel Morrow</div>
    <div class="holder__role">managing director</div>
    <div class="holder__license">License No. 472615</div>
  </div>

  <address class="address">
    48 Ledger Lane<br>
    Millbrook, New York<br>
    12545
  </address>

  <ul class="contacts">
    <li>
      <svg viewBox="0 0 14 14" aria-hidden="true"><rect x="3" y="0.5" width="8" height="13" rx="1.5" fill="none" stroke="#f29a17" stroke-width="1.6"/><circle cx="7" cy="11" r="0.9" fill="#f29a17"/></svg>
      555 214 37 60
    </li>
    <li>
      <svg viewBox="0 0 14 14" aria-hidden="true"><rect x="3.5" y="1" width="7" height="4" fill="#f29a17"/><rect x="1" y="5" width="12" height="6" rx="1" fill="#f29a17"/><rect x="3.5" y="9" width="7" height="4" fill="#f29a17" stroke="#2b3a4d" stroke-width="0.8"/></svg>
      555 738 19 42
    </li>
    <li>
      <svg viewBox="0 0 14 14" aria-hidden="true"><rect x="0.5" y="3" width="13" height="8.5" fill="#f29a17"/><path d="M0.5 3 L7 8 L13.5 3" fill="none" stroke="#2b3a4d" stroke-width="1.2"/></svg>
      dmorrow@tembrikconstruction.com
    </li>
    <li>
      <svg viewBox="0 0 14 14" aria-hidden="true"><circle cx="7" cy="7" r="6" fill="#f29a17"/><path d="M1 7 H13 M7 1 C4 4 4 10 7 13 M7 1 C10 4 10 10 7 13" fill="none" stroke="#2b3a4d" stroke-width="0.9"/></svg>
      www.tembrikconstruction.com
    </li>
  </ul>
</section>

</body>
</html>
```